Rocket business card

Modern business card design, use of color is good with clean space too.

Things to include on card:

Quote: I add fuel to your optometry practice

- Eyewear Sales
- Admin Duties
- Revenue Collection
- Leadership
- Tech Adoption
- COGS Reduction
- Product Sourcing
-Medical Growth

Dalton Vessey, CEO
Glint Harbor
Text Me! 847-302-1964
dalton@glintharbor.example

```html
<!DOCTYPE html>
<html lang="en">
<head>
<meta charset="utf-8">
<title>Glint Harbor — Business Card</title>
<link rel="stylesheet" href="https://fonts.googleapis.com/css2?family=Montserrat:wght@400;500;700&display=swap">
<style>
  :root {
    --page-bg: #2a2a2a;
    --card-bg: #070707;
    --ink-white: #f4f4f4;
    --ink-faint: #1c1c1c;
    --accent-orange: #f29a1f;
    --accent-red: #e2452f;
    --rule-orange: #b5561a;
  }
  * { margin: 0; padding: 0; box-sizing: border-box; }
  html, body {
    width: 1200px; height: 900px; overflow: hidden;
    background: var(--page-bg);
    font-family: "Montserrat", sans-serif;
  }
  .stage {
    width: 1200px; height: 900px;
    display: flex; flex-direction: column; align-items: center; justify-content: center;
    gap: 34px;
  }
  .card {
    position: relative;
    width: 680px; height: 389px;
    background: var(--card-bg);
    overflow: hidden;
  }

  /* Back side: services */
  .back .faint-name {
    position: absolute; left: 0; right: 0; top: 34px;
    text-align: center;
    font-size: 52px; font-weight: 500; letter-spacing: 2px;
    color: var(--ink-faint);
  }
  .back .mark-circle {
    position: absolute; left: 150px; top: 110px;
    width: 190px; height: 190px; border-radius: 50%;
    background: var(--accent-orange);
    border: 14px solid var(--ink-white);
  }
  .back .divider {
    position: absolute; left: 392px; top: 125px;
    width: 2px; height: 160px;
    background: var(--rule-orange);
  }
  .back .services {
    position: absolute; left: 412px; top: 122px;
    list-style: none;
    color: var(--ink-white);
    font-size: 18px; line-height: 21px; letter-spacing: 1px;
  }

  /* Front side: contact */
  .front .brand {
    position: absolute; left: 60px; top: 50px;
    display: flex; align-items: center; gap: 18px;
  }
  .front .brand-dot {
    width: 60px; height: 60px; border-radius: 50%;
    background: var(--accent-orange);
  }
  .front .brand-name {
    font-size: 40px; font-weight: 500; letter-spacing: 2px;
    color: var(--ink-white);
  }
  .front .rule {
    position: absolute; left: 60px; top: 150px;
    width: 580px; height: 1px;
    background: var(--rule-orange);
  }
  .front .person {
    position: absolute; left: 60px; top: 172px;
    font-size: 26px; letter-spacing: 1px;
    color: var(--accent-orange); font-weight: 700;
    text-transform: uppercase;
  }
  .front .person .sep { margin: 0 6px; }
  .front .person .role {
    color: var(--ink-white); font-weight: 400; font-size: 21px;
  }
  .front .contact {
    position: absolute; left: 60px; top: 222px;
    list-style: none;
    color: var(--ink-white);
    font-size: 19px; line-height: 28px; letter-spacing: 0.5px;
  }
  .front .contact li { display: flex; align-items: center; gap: 10px; }
  .front .contact svg { width: 20px; height: 20px; flex: none; }
  .front .contact .prompt { color: var(--accent-orange); }
  .front .quote {
    position: absolute; left: 60px; top: 296px;
    color: var(--ink-white);
    font-size: 21px; line-height: 27px; letter-spacing: 2px;
    text-transform: uppercase;
  }
</style>
</head>
<body>
<main class="stage">
  <section class="card back">
    <div class="faint-name">GLINT HARBOR</div>
    <div class="mark-circle"></div>
    <div class="divider"></div>
    <ul class="services">
      <li>Eyewear Sales</li>
      <li>Admin Duties</li>
      <li>Revenue Collection</li>
      <li>Leadership</li>
      <li>Tech Adoption</li>
      <li>COGS Reduction</li>
      <li>Product Sourcing</li>
      <li>Medical Growth</li>
    </ul>
  </section>

  <section class="card front">
    <div class="brand">
      <div class="brand-dot"></div>
      <div class="brand-name">GLINT HARBOR</div>
    </div>
    <div class="rule"></div>
    <div class="person">Dalton Vessey<span class="sep">|</span><span class="role">CEO</span></div>
    <ul class="contact">
      <li>
        <svg viewBox="0 0 24 24" aria-hidden="true"><path d="M6.6 3.5l3 3.2-1.8 2.3a11 11 0 0 0 7.2 7.2l2.3-1.8 3.2 3-2 2.6c-8 0-15.5-7.5-15.5-15.5z" fill="none" stroke="#e2452f" stroke-width="1.6" stroke-linejoin="round"/></svg>
        <span><span class="prompt">Text Me!</span> 847-302-1964</span>
      </li>
      <li>
        <svg viewBox="0 0 24 24" aria-hidden="true"><rect x="2.5" y="5.5" width="19" height="13" fill="none" stroke="#e2452f" stroke-width="1.6"/><path d="M2.5 5.5l9.5 7.5 9.5-7.5" fill="none" stroke="#e2452f" stroke-width="1.6"/></svg>
        <span>dalton@glintharbor.example</span>
      </li>
    </ul>
    <p class="quote">I add fuel to your<br>optometry practice</p>
  </section>
</main>
</body>
</html>
```